Plume Ovenworks, need a business card design for an innovative bakery

This is a new company out of Boston. We develop innovative baking products. I would you to make a simple card with the colors attached. The design should be modern and fun. Our tag line is " The sweetest way to gift". This should be incorporated into the design.

Industry/Entity Type

Business

Contact Information for Business Card

Plume Ovenworks LLC

Font styles to use
Sans Serif

Requirements
Must have
• Felix Marrow
• Address: 818 Tindle Ave, Suite 2190, Newton MA, 02466
• Phone: 617-5930268
• Emial: FelixMarrow@plumeovenworks.example

```html
<!DOCTYPE html>
<html lang="en">
<head>
<meta charset="utf-8">
<title>Plume Ovenworks – Business Card</title>
<link href="https://fonts.googleapis.com/css2?family=Open+Sans:wght@400;600&display=swap" rel="stylesheet">
<style>
  :root {
    --backdrop: #3b3430;
    --card-navy: #15223a;
    --text-white: #f2f4f7;
    --accent-teal: #7fd3cb;
    --brand-silver: #c9ced6;
    --divider: #2c3a55;
    --icon-glyph: #15223a;
  }
  * { margin: 0; padding: 0; box-sizing: border-box; }
  html, body {
    width: 1200px; height: 844px; overflow: hidden;
    background: var(--backdrop);
    font-family: "Open Sans", Arial, sans-serif;
  }
  .stage {
    width: 1200px; height: 844px;
    display: flex; align-items: center; justify-content: center; gap: 50px;
  }
  .card {
    position: relative;
    width: 540px; height: 309px;
    background: var(--card-navy);
    box-shadow: 0 14px 30px rgba(0,0,0,.45);
    overflow: hidden;
  }
  .brand-name {
    color: var(--brand-silver);
    font-weight: 400;
    font-size: 34px;
    letter-spacing: 1px;
    text-align: center;
    white-space: nowrap;
  }

  /* Front */
  .card-front .brand-name {
    position: absolute; top: 62px; left: 0; right: 0;
  }
  .identity {
    position: absolute; top: 168px; right: 322px;
    text-align: right; white-space: nowrap;
  }
  .person-name { color: var(--text-white); font-weight: 600; font-size: 21px; line-height: 1.15; }
  .person-title { color: var(--accent-teal); font-size: 15px; margin-bottom: 12px; }
  .address { color: var(--text-white); font-size: 15px; line-height: 1.3; font-style: normal; }
  .divider {
    position: absolute; top: 150px; left: 232px; width: 1px; height: 120px;
    background: var(--divider);
  }
  .contact-list {
    position: absolute; top: 150px; left: 246px; right: 16px;
    list-style: none;
  }
  .contact-list li {
    display: flex; align-items: center; gap: 8px;
    color: var(--text-white); font-size: 13px; height: 24px; white-space: nowrap;
  }
  .contact-icon { width: 16px; height: 16px; flex: none; }

  /* Back */
  .card-back .brand-name {
    position: absolute; top: 108px; left: 0; right: 0;
  }
  .tagline {
    position: absolute; top: 190px; left: 0; right: 0;
    text-align: center; color: var(--accent-teal);
    font-size: 15px; letter-spacing: .5px;
  }
</style>
</head>
<body>
<main class="stage">

  <section class="card card-front" aria-label="Business card front">
    <div class="brand-name">Plume Ovenworks</div>

    <div class="identity">
      <div class="person-name">Felix Marrow</div>
      <div class="person-title">Managing Director</div>
      <address class="address">818 Tindle Ave, Suite 2190,<br>Newton MA, 02466</address>
    </div>

    <div class="divider"></div>

    <ul class="contact-list">
      <li>
        <svg class="contact-icon" viewBox="0 0 16 16" aria-hidden="true">
          <rect width="16" height="16" rx="3" fill="var(--accent-teal)"/>
          <path d="M5 3.5 L6.6 3.5 L7.2 6 L6 6.8 Q7 9 9.2 10 L10 8.8 L12.5 9.4 L12.5 11 Q12.5 12.5 11 12.5 Q4 12 3.5 5 Q3.5 3.5 5 3.5Z" fill="var(--icon-glyph)"/>
        </svg>
        617-5930268
      </li>
      <li>
        <svg class="contact-icon" viewBox="0 0 16 16" aria-hidden="true">
          <rect width="16" height="16" rx="3" fill="var(--accent-teal)"/>
          <rect x="5" y="3" width="6" height="3.5" fill="var(--icon-glyph)"/>
          <rect x="3" y="6.5" width="10" height="5" rx="1" fill="var(--icon-glyph)"/>
          <rect x="5" y="10" width="6" height="3" fill="var(--icon-glyph)"/>
        </svg>
        617-5930271
      </li>
      <li>
        <svg class="contact-icon" viewBox="0 0 16 16" aria-hidden="true">
          <rect width="16" height="16" rx="3" fill="var(--accent-teal)"/>
          <rect x="3" y="4.5" width="10" height="7" fill="var(--icon-glyph)"/>
          <path d="M3 4.5 L8 8.5 L13 4.5" fill="none" stroke="var(--accent-teal)" stroke-width="1"/>
        </svg>
        FelixMarrow@plumeovenworks.example
      </li>
      <li>
        <svg class="contact-icon" viewBox="0 0 16 16" aria-hidden="true">
          <rect width="16" height="16" rx="3" fill="var(--accent-teal)"/>
          <path d="M7 9 L9 7 M6.5 7.5 L5 9 Q3.8 10.5 5 11.3 Q6 12.2 7 11 L8.5 9.5 M9.5 8.5 L11 7 Q12.2 5.5 11 4.7 Q10 3.8 9 5 L7.5 6.5" fill="none" stroke="var(--icon-glyph)" stroke-width="1.4" stroke-linecap="round"/>
        </svg>
        www.plumeovenworks.example
      </li>
    </ul>
  </section>

  <section class="card card-back" aria-label="Business card back">
    <div class="brand-name">Plume Ovenworks</div>
    <p class="tagline">The sweetest way to gift</p>
  </section>

</main>
</body>
</html>
```